I need a better looking dashboard for my web application

I have a very table heavy web page that I would like to add a design touch to it. I have the logo and primary colors picked out, I just need some help in adding visual appeal the page. I would also like to add a couple of button to the page as shortcuts. Every spot that has a + sign could have a button added. I would also like to add another graph (the data will be in the uploaded files. Please feel free to ask any questions :-)

```html
<!DOCTYPE html>
<html lang="en">
<head>
<meta charset="utf-8">
<title>Sub Management Dashboard</title>
<link href="https://fonts.googleapis.com/css2?family=Poppins:wght@400;500;600&display=swap" rel="stylesheet">
<style>
:root{
  --purple:#6a4fa3;
  --teal:#2aa8cf;
  --ink:#111;
  --text:#333;
  --muted:#555;
  --line:#e3e3e3;
  --panel-head:#f1f1f1;
  --indigo:#3a2fc4;
  --blue:#4380db;
  --violet:#7b6df0;
  --lilac:#9e95f5;
  --bar-purple:#5b3390;
  --bar-red:#dc3545;
  --bar-green:#28a745;
}
*{box-sizing:border-box;margin:0;padding:0}
html,body{width:1200px;height:892px;overflow:hidden;background:#fff}
body{font-family:"Poppins",sans-serif;color:var(--text);position:relative}
.abs{position:absolute}
.brand{left:28px;top:14px;display:flex;align-items:center;gap:8px;font-size:30px;font-weight:500;color:var(--purple)}
.brand-dot{width:28px;height:28px;border-radius:50%;background:var(--teal)}
.page-title{left:282px;top:22px;font-size:21px;font-weight:500;color:var(--ink)}
.nav{top:26px;font-size:12px;color:var(--ink);display:flex;align-items:center;gap:4px}
.nav svg{width:11px;height:11px}
.staff-btn{left:847px;top:19px;width:129px;height:32px;background:#222;color:#fff;font-size:12px;display:flex;align-items:center;justify-content:center;gap:5px;border-radius:2px 2px 0 0}
.dropdown{left:847px;top:51px;width:129px;height:61px;background:var(--teal);color:#222;font-size:9px;padding:13px 0 0 18px;line-height:23px;border-radius:0 0 3px 3px;z-index:2}
.tabbar{left:23px;top:67px;width:1156px;height:32px;background:var(--purple);border-radius:2px}
.tab{position:absolute;top:0;height:32px;line-height:32px;font-size:12px;font-weight:500;padding:0 16px}
.tab.active{left:0;width:103px;background:var(--teal);color:#fff}
.tab.plain{left:118px;color:#c9bde4}
.section-title{font-size:15px;font-weight:500;color:var(--ink)}
.panel{border:1px solid #ddd;box-shadow:0 1px 3px rgba(0,0,0,.12);background:#fff}
.thead{position:absolute;left:0;right:0;top:0;background:var(--panel-head);font-size:10px;color:var(--ink)}
.add-btn{position:absolute;left:0;top:0;width:58px;height:31px;background:var(--teal);color:#fff;font-size:8.5px;font-weight:500;display:flex;align-items:center;justify-content:center}
.cell{position:absolute;white-space:nowrap}
.rows{position:absolute;left:0;right:0;font-size:9px;color:var(--text)}
.row{position:absolute;left:0;right:0;height:20px}
.row .cell{top:4px}
.ico{position:absolute;top:4px;width:11px;height:11px}
.cast{position:absolute;left:15px;font-size:8.5px;color:#444}
.btn{position:absolute;width:129px;height:32px;color:#fff;font-size:12px;font-weight:500;display:flex;align-items:center;justify-content:center;border-radius:2px}
.photo{position:absolute;width:26px;height:26px;background:linear-gradient(135deg,#7a3b2e,#c9836b)}
.legend{position:absolute;font-size:7px;color:#444;display:flex;align-items:center;gap:3px}
.legend i{width:4px;height:4px;border-radius:50%;display:inline-block}
.sumrow{position:absolute;left:16px;right:16px;height:24px;font-size:9px;color:#333;border-bottom:1px solid var(--line)}
.sumrow span{position:absolute;top:4px}
.footer{left:0;width:1200px;top:863px;text-align:center;font-size:10px;color:#222}
.tag{right:6px;top:874px;font-size:11px;color:#222}
</style>
</head>
<body>

<div class="abs brand"><span class="brand-dot"></span>ShiftCover</div>
<div class="abs page-title">Sub Management</div>

<div class="abs nav" style="left:530px"><svg viewBox="0 0 12 12"><path d="M1 6 6 1.5 11 6M2.5 5v5.5h7V5" fill="none" stroke="#4a6fb5"/></svg>Home <svg viewBox="0 0 12 12"><path d="M2 4l4 4 4-4" fill="none" stroke="#111" stroke-width="1.5"/></svg></div>
<div class="abs nav" style="left:614px"><svg viewBox="0 0 12 12"><rect x="1" y="2.5" width="10" height="7" fill="none" stroke="#4a6fb5"/><path d="M1 2.5 6 6.5 11 2.5" fill="none" stroke="#4a6fb5"/></svg>Demo Outbox</div>
<div class="abs nav" style="left:720px"><svg viewBox="0 0 12 12"><path d="M6 11.5C3 8 2.5 6.5 2.5 5a3.5 3.5 0 0 1 7 0c0 1.5-.5 3-3.5 6.5z" fill="#4a6fb5"/><circle cx="6" cy="5" r="1.2" fill="#fff"/></svg>Location Admin <svg viewBox="0 0 12 12"><path d="M2 4l4 4 4-4" fill="none" stroke="#111" stroke-width="1.5"/></svg></div>
<div class="abs staff-btn"><svg width="10" height="10" viewBox="0 0 12 12"><circle cx="6" cy="4" r="2.5" fill="none" stroke="#fff"/><path d="M1.5 11.5c0-3 2-4.5 4.5-4.5s4.5 1.5 4.5 4.5z" fill="none" stroke="#fff"/></svg>Regular Staff<svg width="10" height="10" viewBox="0 0 12 12"><path d="M2 4l4 4 4-4" fill="none" stroke="#fff" stroke-width="1.6"/></svg></div>
<div class="abs dropdown">Manage Regular Staff<br>Leave Requests</div>
<div class="abs nav" style="left:993px"><svg viewBox="0 0 12 12"><circle cx="4" cy="3.5" r="2" fill="#111"/><circle cx="8.5" cy="4" r="1.7" fill="#111"/><path d="M0.5 11c0-2.5 1.5-4 3.5-4s3.5 1.5 3.5 4zM7 11c0-2 1-3 2-3s2.5 1 2.5 3z" fill="#111"/></svg>dn.manager@example.com <svg viewBox="0 0 12 12"><path d="M2 4l4 4 4-4" fill="none" stroke="#111" stroke-width="1.5"/></svg></div>

<div class="abs tabbar"><div class="tab active">Dashboard</div><div class="tab plain">Calender</div></div>

<!-- Managed Openings -->
<div class="abs section-title" style="left:34px;top:112px">Managed Openings</div>
<div class="abs panel" style="left:28px;top:139px;width:565px;height:192px">
  <div class="thead" style="height:31px">
    <div class="add-btn">+ Add</div>
    <span class="cell" style="left:76px;top:7px">Category</span>
    <span class="cell" style="left:150px;top:7px">Regular Staff</span>
    <span class="cell" style="left:232px;top:7px">Status</span>
    <span class="cell" style="left:297px;top:7px">Summary</span>
    <svg class="cell" style="left:364px;top:6px" width="10" height="13" viewBox="0 0 10 13"><path d="M5 12V2M1.5 5.5 5 1.5l3.5 4" fill="none" stroke="#2bb673" stroke-width="1.2"/></svg>
    <span class="cell" style="left:394px;top:8px">Location</span>
    <span class="cell" style="left:462px;top:7px">Time Slots Summary</span>
  </div>
  <div class="cast" style="top:35px">Cast</div>
  <svg class="abs" style="left:264px;top:38px" width="8" height="6" viewBox="0 0 8 6"><path d="M1 1.5 4 4.5 7 1.5" fill="none" stroke="#333"/></svg>
  <div class="rows" style="top:45px">
    <div class="row" style="top:0"><svg class="ico" style="left:9px" viewBox="0 0 12 12"><path d="M2 10h8M2.5 8.5l1-2.5 5-5 1.5 1.5-5 5z" fill="none" stroke="#2a6fbf" stroke-width="1.1"/></svg><svg class="ico" style="left:49px" viewBox="0 0 12 12"><path d="M2 3h8M4.5 3V1.5h3V3M3 3.5l.7 7.5h4.6l.7-7.5z" fill="#111"/></svg><span class="cell" style="left:76px">Food Service</span><span class="cell" style="left:150px">Extra duty</span><span class="cell" style="left:232px">Assigned</span><span class="cell" style="left:297px">Immediate Need...</span><span class="cell" style="left:394px">LiE</span><span class="cell" style="left:462px">12/30 - 01/01 (2h 30m)</span></div>
    <div class="row" style="top:20.5px"><svg class="ico" style="left:9px" viewBox="0 0 12 12"><path d="M2 10h8M2.5 8.5l1-2.5 5-5 1.5 1.5-5 5z" fill="none" stroke="#2a6fbf" stroke-width="1.1"/></svg><svg class="ico" style="left:49px" viewBox="0 0 12 12"><path d="M2 3h8M4.5 3V1.5h3V3M3 3.5l.7 7.5h4.6l.7-7.5z" fill="#111"/></svg><span class="cell" style="left:76px">Teacher</span><span class="cell" style="left:150px">Naomi Wills</span><span class="cell" style="left:232px">Available</span><span class="cell" style="left:297px">Immediate Need...</span><span class="cell" style="left:394px">WDMS</span><span class="cell" style="left:462px">12/30 - 01/01 (2h 30m)</span></div>
    <div class="row" style="top:41px"><svg class="ico" style="left:9px" viewBox="0 0 12 12"><path d="M2 10h8M2.5 8.5l1-2.5 5-5 1.5 1.5-5 5z" fill="none" stroke="#2a6fbf" stroke-width="1.1"/></svg><svg class="ico" style="left:49px" viewBox="0 0 12 12"><path d="M2 3h8M4.5 3V1.5h3V3M3 3.5l.7 7.5h4.6l.7-7.5z" fill="#111"/></svg><span class="cell" style="left:76px">Bus Driver</span><span class="cell" style="left:150px">Extra duty</span><span class="cell" style="left:232px">Available</span><span class="cell" style="left:297px">Immediate Need...</span><span class="cell" style="left:394px">WDMS</span><span class="cell" style="left:462px">12/30 - 01/01 (2h 30m)</span></div>
    <div class="row" style="top:61.5px"><svg class="ico" style="left:9px" viewBox="0 0 12 12"><path d="M2 10h8M2.5 8.5l1-2.5 5-5 1.5 1.5-5 5z" fill="none" stroke="#2a6fbf" stroke-width="1.1"/></svg><svg class="ico" style="left:49px" viewBox="0 0 12 12"><path d="M2 3h8M4.5 3V1.5h3V3M3 3.5l.7 7.5h4.6l.7-7.5z" fill="#111"/></svg><span class="cell" style="left:76px">Custodian</span><span class="cell" style="left:150px">Extra duty</span><span class="cell" style="left:232px">Available</span><span class="cell" style="left:297px">Immediate Need...</span><span class="cell" style="left:394px">FMS</span><span class="cell" style="left:462px">12/30 - 01/01 (2h 30m)</span></div>
    <div class="row" style="top:82px"><svg class="ico" style="left:9px" viewBox="0 0 12 12"><path d="M2 10h8M2.5 8.5l1-2.5 5-5 1.5 1.5-5 5z" fill="none" stroke="#2a6fbf" stroke-width="1.1"/></svg><svg class="ico" style="left:49px" viewBox="0 0 12 12"><path d="M2 3h8M4.5 3V1.5h3V3M3 3.5l.7 7.5h4.6l.7-7.5z" fill="#111"/></svg><span class="cell" style="left:76px">Teacher's Aide</span><span class="cell" style="left:150px">Extra duty</span><span class="cell" style="left:232px">Available</span><span class="cell" style="left:297px">Immediate Need...</span><span class="cell" style="left:394px">FMS</span><span class="cell" style="left:462px">12/30 - 01/01 (2h 30m)</span></div>
    <div class="row" style="top:103px"><svg class="ico" style="left:9px" viewBox="0 0 12 12"><path d="M2 10h8M2.5 8.5l1-2.5 5-5 1.5 1.5-5 5z" fill="none" stroke="#2a6fbf" stroke-width="1.1"/></svg><svg class="ico" style="left:49px" viewBox="0 0 12 12"><path d="M2 3h8M4.5 3V1.5h3V3M3 3.5l.7 7.5h4.6l.7-7.5z" fill="#111"/></svg><span class="cell" style="left:76px">Food Service</span><span class="cell" style="left:150px">Naomi Wills</span><span class="cell" style="left:232px">Available</span><span class="cell" style="left:297px">Immediate Need...</span><span class="cell" style="left:394px">FMS</span><span class="cell" style="left:462px">12/30 - 01/01 (2h 30m)</span></div>
    <div class="row" style="top:123.5px"><svg class="ico" style="left:9px" viewBox="0 0 12 12"><path d="M2 10h8M2.5 8.5l1-2.5 5-5 1.5 1.5-5 5z" fill="none" stroke="#2a6fbf" stroke-width="1.1"/></svg><svg class="ico" style="left:49px" viewBox="0 0 12 12"><path d="M2 3h8M4.5 3V1.5h3V3M3 3.5l.7 7.5h4.6l.7-7.5z" fill="#111"/></svg><span class="cell" style="left:76px">Teacher's Aide</span><span class="cell" style="left:150px">Naomi Wills</span><span class="cell" style="left:232px">Available</span><span class="cell" style="left:297px">Immediate Need...</span><span class="cell" style="left:394px">LiE</span><span class="cell" style="left:462px">12/30 - 01/01 (2h 30m)</span></div>
  </div>
</div>

<!-- Location Overview -->
<div class="abs section-title" style="left:614px;top:112px">Location Overview</div>
<div class="abs panel" style="left:608px;top:139px;width:566px;height:192px">
  <div class="thead" style="height:24px"><span class="cell" style="left:19px;top:5px;font-size:9px">Leave Request/Openings/Assignments</span></div>
  <div class="legend" style="left:257px;top:27px"><i style="background:var(--bar-purple)"></i>Openings; Unfilled</div>
  <div class="legend" style="left:360px;top:27px"><i style="background:var(--bar-green)"></i>Openings; Filled</div>
  <div class="legend" style="left:456px;top:27px"><i style="background:var(--bar-red)"></i>LeaveRequests; Pending</div>
  <svg class="abs" style="left:0;top:0" width="566" height="192" viewBox="0 0 566 192">
    <g font-family="Poppins,sans-serif" font-size="8" fill="#333">
      <text x="20" y="49">10</text><text x="23" y="72">8</text><text x="23" y="94">6</text><text x="23" y="117">4</text><text x="23" y="139">2</text><text x="23" y="161">0</text>
    </g>
    <g stroke="#ececec"><path d="M38 46H550M38 68.5H550M38 91H550M38 113.5H550M38 136H550M38 158.5H550"/></g>
    <rect x="64" y="110" width="21" height="48.5" fill="var(--bar-purple)"/>
    <rect x="64" y="102.5" width="21" height="7.5" fill="var(--bar-green)"/>
    <rect x="96" y="102.5" width="21" height="56" fill="var(--bar-red)"/>
    <rect x="249" y="91" width="21" height="67.5" fill="var(--bar-purple)"/>
    <rect x="281" y="102.5" width="21" height="56" fill="var(--bar-red)"/>
    <rect x="443" y="72" width="21" height="86.5" fill="var(--bar-purple)"/>
    <g font-family="Poppins,sans-serif" font-size="8.5" fill="#333" text-anchor="middle">
      <text x="96" y="182">Lake Jonas Elementary</text><text x="278" y="182">Feestbery Middle School</text><text x="472" y="182">West Devante Middle School</text>
    </g>
  </svg>
</div>

<!-- Regular Staff Leave Request -->
<div class="abs section-title" style="left:34px;top:374px">Regular Staff Leave Request</div>
<div class="abs panel" style="left:28px;top:400px;width:565px;height:185px">
  <div class="thead" style="height:33px">
    <div class="add-btn" style="height:33px">+ Add</div>
    <span class="cell" style="left:82px;top:11px">Status</span>
    <span class="cell" style="left:161px;top:11px">Full Name</span>
    <div style="position:absolute;left:250px;top:0;width:192px;height:33px;border-left:1px solid #ddd;border-right:1px solid #ddd">
      <div style="height:15px;border-bottom:1px solid #ddd;text-align:center;padding-top:1px">Opening</div>
      <span class="cell" style="left:11px;top:18px">Assignment</span><span class="cell" style="left:106px;top:18px">Prearranged Sub</span>
    </div>
    <span class="cell" style="left:462px;top:14px">Time Slots Summary</span>
  </div>
  <div class="cast" style="top:38px">Cast</div>
  <div class="rows" style="top:48px">
    <div class="row" style="top:0"><svg class="ico" style="left:9px" viewBox="0 0 12 12"><path d="M2 10h8M2.5 8.5l1-2.5 5-5 1.5 1.5-5 5z" fill="none" stroke="#2a6fbf" stroke-width="1.1"/></svg><svg class="ico" style="left:41px;width:12px" viewBox="0 0 12 12"><path d="M.5 6C2 3.5 4 2.5 6 2.5S10 3.5 11.5 6C10 8.5 8 9.5 6 9.5S2 8.5.5 6z" fill="#111"/><circle cx="6" cy="6" r="1.6" fill="#fff"/></svg><span class="cell" style="left:82px">Pending</span><span class="cell" style="left:161px">Alan Bowman</span><span class="cell" style="left:260px">N/A</span><span class="cell" style="left:371px">N/A</span><span class="cell" style="left:462px">12/30 - 01/01 (2h 30m)</span></div>
    <div class="row" style="top:20.5px"><svg class="ico" style="left:9px" viewBox="0 0 12 12"><path d="M2 10h8M2.5 8.5l1-2.5 5-5 1.5 1.5-5 5z" fill="none" stroke="#2a6fbf" stroke-width="1.1"/></svg><svg class="ico" style="left:41px;width:12px" viewBox="0 0 12 12"><path d="M.5 6C2 3.5 4 2.5 6 2.5S10 3.5 11.5 6C10 8.5 8 9.5 6 9.5S2 8.5.5 6z" fill="#111"/><circle cx="6" cy="6" r="1.6" fill="#fff"/></svg><span class="cell" style="left:82px">Pending</span><span class="cell" style="left:161px">Glen Gilbert</span><span class="cell" style="left:260px;top:7px">N/A</span><span class="cell" style="left:371px;top:7px">N/A</span><span class="cell" style="left:462px">12/30 - 01/01 (2h 30m)</span></div>
    <div class="row" style="top:41px"><svg class="ico" style="left:9px" viewBox="0 0 12 12"><path d="M2 10h8M2.5 8.5l1-2.5 5-5 1.5 1.5-5 5z" fill="none" stroke="#2a6fbf" stroke-width="1.1"/></svg><svg class="ico" style="left:41px;width:12px" viewBox="0 0 12 12"><path d="M.5 6C2 3.5 4 2.5 6 2.5S10 3.5 11.5 6C10 8.5 8 9.5 6 9.5S2 8.5.5 6z" fill="#111"/><circle cx="6" cy="6" r="1.6" fill="#fff"/></svg><span class="cell" style="left:82px">Pending</span><span class="cell" style="left:161px">Erica Barnes</span><span class="cell" style="left:260px;top:6px">Counselor</span><span class="cell" style="left:462px">12/30 - 01/01 (2h 30m)</span></div>
    <div class="row" style="top:61.5px"><svg class="ico" style="left:9px" viewBox="0 0 12 12"><path d="M2 10h8M2.5 8.5l1-2.5 5-5 1.5 1.5-5 5z" fill="none" stroke="#2a6fbf" stroke-width="1.1"/></svg><svg class="ico" style="left:41px;width:12px" viewBox="0 0 12 12"><path d="M.5 6C2 3.5 4 2.5 6 2.5S10 3.5 11.5 6C10 8.5 8 9.5 6 9.5S2 8.5.5 6z" fill="#111"/><circle cx="6" cy="6" r="1.6" fill="#fff"/></svg><span class="cell" style="left:82px">Pending</span><span class="cell" style="left:161px">Virginia Waldon</span><span class="cell" style="left:260px">N/A</span><span class="cell" style="left:371px">N/A</span><span class="cell" style="left:462px">12/30 - 01/01 (2h 30m)</span></div>
    <div class="row" style="top:82px"><svg class="ico" style="left:9px" viewBox="0 0 12 12"><path d="M2 10h8M2.5 8.5l1-2.5 5-5 1.5 1.5-5 5z" fill="none" stroke="#2a6fbf" stroke-width="1.1"/></svg><svg class="ico" style="left:41px;width:12px" viewBox="0 0 12 12"><path d="M.5 6C2 3.5 4 2.5 6 2.5S10 3.5 11.5 6C10 8.5 8 9.5 6 9.5S2 8.5.5 6z" fill="#111"/><circle cx="6" cy="6" r="1.6" fill="#fff"/></svg><span class="cell" style="left:82px">Pending</span><span class="cell" style="left:161px">Gary Hamilton</span><span class="cell" style="left:260px;top:6px">Administrator</span><span class="cell" style="left:371px">Mary Griffiths</span><span class="cell" style="left:462px">12/30 - 01/01 (2h 30m)</span></div>
    <div class="row" style="top:103px"><svg class="ico" style="left:9px" viewBox="0 0 12 12"><path d="M2 10h8M2.5 8.5l1-2.5 5-5 1.5 1.5-5 5z" fill="none" stroke="#2a6fbf" stroke-width="1.1"/></svg><svg class="ico" style="left:41px;width:12px" viewBox="0 0 12 12"><path d="M.5 6C2 3.5 4 2.5 6 2.5S10 3.5 11.5 6C10 8.5 8 9.5 6 9.5S2 8.5.5 6z" fill="#111"/><circle cx="6" cy="6" r="1.6" fill="#fff"/></svg><span class="cell" style="left:82px">Pending</span><span class="cell" style="left:161px">John Tuller</span><span class="cell" style="left:260px;top:6px">Administrator</span><span class="cell" style="left:462px">12/30 - 01/01 (2h 30m)</span></div>
  </div>
</div>

<!-- Pending Profile Images -->
<div class="abs section-title" style="left:618px;top:372px">Pending Profile Images</div>
<div class="abs panel" style="left:609px;top:400px;width:566px;height:185px">
  <div class="thead" style="height:33px">
    <span class="cell" style="left:22px;top:11px">Last Name</span>
    <span class="cell" style="left:127px;top:11px">First Name</span>
    <div style="position:absolute;left:250px;top:0;width:193px;height:33px;border-left:1px solid #ddd;border-right:1px solid #ddd">
      <div style="height:15px;border-bottom:1px solid #ddd;text-align:center;padding-top:1px">Profile Images</div>
      <span class="cell" style="left:11px;top:18px">Pending</span><span class="cell" style="left:102px;top:18px">Previously Verfied</span>
    </div>
    <span class="cell" style="left:490px;top:10px">Options</span>
  </div>
  <div class="rows" style="top:40px">
    <div class="row" style="top:0"><span class="cell" style="left:22px">Walters</span><span class="cell" style="left:127px">Kim</span><div class="photo" style="left:263px;top:0" role="img" aria-label="Pending profile photo for Kim Walters"></div><span class="cell" style="left:352px">None Available</span></div>
    <div class="row" style="top:37px"><span class="cell" style="left:22px">Stevents</span><span class="cell" style="left:127px">Mason</span><div class="photo" style="left:261px;top:0;background:linear-gradient(135deg,#c8a48c,#e9d6c6)" role="img" aria-label="Pending profile photo for Mason Stevents"></div><span class="cell" style="left:352px">None Available</span></div>
    <div class="row" style="top:73px"><span class="cell" style="left:22px">Mora'es</span><span class="cell" style="left:127px">June</span><div class="photo" style="left:263px;top:0;background:linear-gradient(135deg,#5a2f28,#b98070)" role="img" aria-label="Pending profile photo for June Mora'es"></div><span class="cell" style="left:352px">None Available</span></div>
    <div class="row" style="top:110px"><span class="cell" style="left:22px">Steachers</span><span class="cell" style="left:127px">Priscilla</span><div class="photo" style="left:263px;top:0;background:linear-gradient(135deg,#4a1f1c,#a05a4a)" role="img" aria-label="Pending profile photo for Priscilla Steachers"></div><span class="cell" style="left:352px">None Available</span></div>
  </div>
  <svg class="abs" style="left:488px;top:40px" width="50" height="125" viewBox="0 0 50 125">
    <g fill="none" stroke="#333" stroke-width=".9">
      <circle cx="8" cy="8" r="7"/><path d="M4.5 8.2l2.4 2.3 4.6-4.6"/><circle cx="32" cy="8" r="7"/><path d="M29.5 5.5l5 5M34.5 5.5l-5 5"/>
      <circle cx="8" cy="44" r="7"/><path d="M4.5 44.2l2.4 2.3 4.6-4.6"/><circle cx="32" cy="44" r="7"/><path d="M29.5 41.5l5 5M34.5 41.5l-5 5"/>
      <circle cx="8" cy="80" r="7"/><path d="M4.5 80.2l2.4 2.3 4.6-4.6"/><circle cx="32" cy="80" r="7"/><path d="M29.5 77.5l5 5M34.5 77.5l-5 5"/>
      <circle cx="8" cy="116" r="7"/><path d="M4.5 116.2l2.4 2.3 4.6-4.6"/><circle cx="32" cy="116" r="7"/><path d="M29.5 113.5l5 5M34.5 113.5l-5 5"/>
    </g>
  </svg>
</div>

<!-- Today's Summary -->
<div class="abs section-title" style="left:34px;top:619px">Today's Summary</div>
<div class="abs panel" style="left:28px;top:645px;width:565px;height:185px">
  <div class="legend" style="left:12px;top:17px"><i style="background:var(--indigo)"></i>Unfilled</div>
  <div class="legend" style="left:66px;top:17px"><i style="background:var(--violet)"></i>Filled</div>
  <div class="legend" style="left:110px;top:17px"><i style="background:var(--lilac)"></i>No Sub Needed</div>
  <div class="legend" style="left:190px;top:17px"><i style="background:var(--blue)"></i>Total</div>
  <span class="abs" style="left:15px;top:37px;font-size:8.5px;color:#333">Jan 22</span>
  <svg class="abs" style="left:47px;top:38px" width="498" height="12" viewBox="0 0 498 12">
    <rect x="0" y="0.5" width="497" height="11" rx="5.5" fill="var(--blue)"/>
    <path d="M5.5.5H297V11.5H5.5A5.5 5.5 0 0 1 5.5.5z" fill="var(--lilac)"/>
    <path d="M5.5.5H243V11.5H5.5A5.5 5.5 0 0 1 5.5.5z" fill="var(--violet)"/>
    <path d="M5.5.5H38V11.5H5.5A5.5 5.5 0 0 1 5.5.5z" fill="var(--indigo)"/>
  </svg>
  <div class="abs" style="left:0;width:565px;top:72px;text-align:center;font-size:9.5px;color:#222">Monthly Summary</div>
  <div class="sumrow" style="top:96px"><span style="left:4px">Total Jobs</span><span style="left:288px">45</span></div>
  <div class="sumrow" style="top:120px"><span style="left:4px">Filled Jobs</span><span style="left:288px">data</span></div>
  <div class="sumrow" style="top:144px;border-bottom:none"><span style="left:4px">No Sub Needed</span><span style="left:288px">data</span></div>
</div>

<!-- Shortcut buttons -->
<div class="btn" style="left:643px;top:701px;background:var(--indigo)">Create Absence</div>
<div class="btn" style="left:796px;top:701px;background:var(--blue)">Approve 8</div>
<div class="btn" style="left:643px;top:753px;background:var(--lilac)">Create Vacancy</div>
<div class="btn" style="left:796px;top:753px;background:var(--violet)">Approve 3</div>

<!-- Monthly Fill Rate -->
<div class="abs section-title" style="left:951px;top:619px">Monthly Fill Rate</div>
<svg class="abs" style="left:978px;top:662px" width="184" height="184" viewBox="0 0 184 184">
  <g transform="rotate(-90 92 92)" fill="none" stroke-width="50">
    <circle cx="92" cy="92" r="67" stroke="var(--indigo)" stroke-dasharray="168.4 252.6"/>
    <circle cx="92" cy="92" r="67" stroke="var(--violet)" stroke-dasharray="138.9 282.1" stroke-dashoffset="-168.4"/>
    <circle cx="92" cy="92" r="67" stroke="var(--lilac)" stroke-dasharray="113.7 307.3" stroke-dashoffset="-307.3"/>
  </g>
  <g stroke="#fff" stroke-width="1.5"><path d="M92 0V42M125 131L160 167M42 92H0"/></g>
  <g font-family="Poppins,sans-serif" font-size="9" fill="#fff" font-weight="500">
    <text x="146" y="70">Filled</text><text x="146" y="84">40%</text>
    <text x="74" y="158">Open</text><text x="74" y="172">33%</text>
    <text x="28" y="62">No Sub</text><text x="28" y="76">27%</text>
  </g>
</svg>

<div class="abs footer">Copyright © Northfield Systems. All rights reserved. (v.0.8.4)</div>
<div class="abs tag">C44</div>

</body>
</html>
```